■依頼の目的
2月に出版予定の電子書籍

タイトル:後悔しない住まい手配ガイド決定版2021
サブタイトル:[特集]三世代でつなぐ暮らし設計
著者:一級建築士 柚木湊

キャッチコピー:コロナ対応住宅チェックリスト付き!

※追加テキスト
家づくりの補助金
4月に省エネ説明義務化
IoT住宅の現在

キャッチコピー等の配置はPDFに記載

の表紙デザインをお願いします。

■本の内容
・年一回発行する雑誌形式の電子書籍
・住宅会社選びの方法を紹介
・特集記事や時事ネタも扱う

■デザイン要望
・30代~40代の子育て夫婦に好まれるデザインを希望
・LivoMarqueのようなお洒落な家づくり雑誌の雰囲気
・過去の4作品との差別化(過去表紙はPDFに)
・最新作であることがわかるよう「2021」を目立つように

■キャッチ等の変更の可能性あり
お願いする方が決まった後、キャッチコピーなどの文字を若干変更する可能性があります。

■添付ファイルについて
・必要な配置をPDFに添付しています
・ロゴのaiデータ添付します

その他何かご不明な点がございましたら、お気軽にご質問下さい。
よろしくお願いいたします。
・Pebble magazine というタイトルの色は、変えるようにしてください。
年一回の雑誌なので、毎年、ちがう色を使っています。
過去の作品と被らないように色提案をお願いします。
・文字はスマホで見た時にも、読めることを意識してください。
・背景の写真・イラストのセレクトが重要になります。livoなどのインテリア雑誌などを参考にしてください。

写真の選び方が秀逸でした。
シンメトリーを意識したモダンな建物外観が素晴らしく、それを引き立たせるようなデザインで、見た瞬間、これしかないと思わせるものでした。
今回は、私のメルマガ読者200人にアンケートを行って半数の方がこのデザインを支持しました。

この度は、沢山のご提案を頂きありがとうございました!
毎年、出版しているシリーズでしたが、雰囲気を一新したいことからコンペを使わせて頂きましたが、様々なデザイン提案を頂き、とても参考になりました。
今後もコンペを使わせて頂きますので、引き続きよろしくお願いいたします!

```html
<!DOCTYPE html>
<html lang="ja">
<head>
<meta charset="utf-8">
<title>Pebble magazine vol.5 2021</title>
<link rel="stylesheet" href="https://fonts.googleapis.com/css2?family=Noto+Serif+JP:wght@600;700;900&family=Noto+Sans+JP:wght@500;700&family=Playfair+Display:ital,wght@0,700;1,400&display=swap">
<style>
  :root {
    --wall-light: #e6e6e4;
    --wall: #d8d8d6;
    --wall-shadow: #c6c4c0;
    --cushion: #b9b7b3;
    --sofa: #a8764a;
    --sofa-dark: #7e5636;
    --wood: #c29a6c;
    --rug: #d9d5cf;
    --floor: #e4e1dc;
    --ink: #1c1c1c;
    --logo-gold: #b08a4a;
    --badge-red: #d8262c;
    --white: #ffffff;
  }
  * { margin: 0; padding: 0; box-sizing: border-box; }
  html, body { width: 725px; height: 1200px; overflow: hidden; background: var(--wall); }
  .cover {
    position: relative;
    width: 725px;
    height: 1200px;
    overflow: hidden;
    color: var(--ink);
    font-family: "Noto Serif JP", serif;
  }
  .cover-photo {
    position: absolute;
    inset: 0;
    background:
      radial-gradient(ellipse 60% 16% at 50% 64%, rgba(205,203,199,0.9) 0%, rgba(205,203,199,0) 100%),
      radial-gradient(ellipse 70% 14% at 50% 74%, rgba(168,118,74,0.95) 0%, rgba(168,118,74,0) 100%),
      radial-gradient(ellipse 45% 10% at 45% 84%, rgba(194,154,108,0.7) 0%, rgba(194,154,108,0) 100%),
      linear-gradient(180deg,
        var(--wall-light) 0%,
        var(--wall) 40%,
        var(--wall-shadow) 52%,
        var(--cushion) 58%,
        var(--sofa) 68%,
        var(--sofa-dark) 76%,
        #a99a8a 82%,
        var(--rug) 89%,
        var(--floor) 100%);
  }
  .masthead {
    position: absolute;
    left: 86px;
    top: 18px;
    font-family: "Playfair Display", serif;
    font-weight: 700;
    color: var(--logo-gold);
    line-height: 0.95;
  }
  .masthead-name { font-size: 118px; letter-spacing: -1px; }
  .masthead-sub { font-size: 52px; padding-left: 140px; }
  .issue-label {
    position: absolute;
    left: 456px;
    top: 44px;
    font-family: "Noto Sans JP", sans-serif;
    font-weight: 500;
    font-size: 13px;
    color: #4a4a4a;
    line-height: 1.3;
  }
  .news-list {
    position: absolute;
    right: 30px;
    top: 138px;
    list-style: none;
    text-align: right;
    font-weight: 700;
    font-size: 19px;
    line-height: 1.45;
  }
  .headline {
    position: absolute;
    left: 90px;
    top: 240px;
    font-weight: 900;
    font-size: 66px;
    line-height: 1.2;
    letter-spacing: 0;
  }
  .feature {
    position: absolute;
    left: 90px;
    top: 500px;
    display: flex;
    align-items: center;
    gap: 12px;
    font-weight: 700;
    font-size: 36px;
    line-height: 1;
  }
  .feature-tag {
    border: 3px solid var(--ink);
    padding: 2px 6px 4px;
    font-size: 32px;
  }
  .author {
    position: absolute;
    right: 100px;
    top: 556px;
    font-weight: 700;
    font-size: 32px;
    display: flex;
    align-items: baseline;
    gap: 12px;
  }
  .author-title { font-size: 16px; }
  .year {
    position: absolute;
    left: 0;
    right: 0;
    top: 1040px;
    text-align: center;
    font-family: "Playfair Display", serif;
    font-weight: 700;
    font-size: 116px;
    line-height: 1;
    letter-spacing: 2px;
  }
  .tagline {
    position: absolute;
    left: 0;
    right: 0;
    top: 1160px;
    text-align: center;
    font-family: "Playfair Display", serif;
    font-style: italic;
    font-size: 19px;
  }
  .badge {
    position: absolute;
    left: 626px;
    top: 1026px;
    width: 88px;
    height: 88px;
    border-radius: 50%;
    background: var(--badge-red);
    color: var(--white);
    font-family: "Noto Sans JP", sans-serif;
    font-weight: 700;
    font-size: 13px;
    line-height: 1.25;
    display: flex;
    align-items: center;
    justify-content: center;
    text-align: center;
  }
</style>
</head>
<body>
<main class="cover">
  <div class="cover-photo" role="img" aria-label="明るいリビングの写真:グレーの壁の前にクッションを並べたキャメル色の革ソファ、木のサイドテーブル、積んだ本、ラグの上の丸いローテーブル"></div>

  <div class="masthead">
    <div class="masthead-name">Pebble</div>
    <div class="masthead-sub">magazine</div>
  </div>
  <div class="issue-label">[ペブルマガジン]<br>vol.5 2021</div>

  <ul class="news-list">
    <li>家づくりの補助金</li>
    <li>4月に省エネ説明義務化</li>
    <li>IoT住宅の現在</li>
  </ul>

  <h1 class="headline">後悔しない<br>住まい手配ガイド<br>決定版</h1>

  <p class="feature"><span class="feature-tag">特集</span><span>三世代でつなぐ暮らし設計</span></p>
  <p class="author"><span class="author-title">一級建築士</span><span>柚木 湊</span></p>

  <div class="badge">コロナ<br>対応住宅<br>チェック<br>リスト付き!</div>

  <p class="year">2021</p>
  <p class="tagline">How to plan a home without regret</p>
</main>
</body>
</html>
```